KVRo Business Cards

We need a business card design. We are a Technology (Audio Visual) design, sales and installation company. Looking for a double sided design, clean

Contact Information for Business Card

Clean, modern look, 2 sided

Font styles to use
Sans Serif

```html
<!DOCTYPE html>
<html lang="en">
<head>
<meta charset="utf-8">
<title>KVRo Business Cards</title>
<link href="https://fonts.googleapis.com/css2?family=Jost:wght@400;600;700&display=swap" rel="stylesheet">
<style>
  :root {
    --backdrop: #d8d6d4;
    --navy: #2c4957;
    --orange: #f09631;
    --paper: #ecebe8;
  }
  * { margin: 0; padding: 0; box-sizing: border-box; }
  html, body {
    width: 1200px; height: 900px; overflow: hidden;
    background: var(--backdrop);
    font-family: "Jost", "Futura", sans-serif;
  }
  .card {
    position: absolute;
    left: 352px;
    width: 496px;
    height: 284px;
  }
  .card--front { top: 149px; background: var(--navy); }
  .card--back { top: 485px; background: var(--orange); }

  .wordmark {
    position: absolute;
    font-weight: 600;
    line-height: 1;
    letter-spacing: -1px;
  }
  .card--front .wordmark {
    left: 39px; top: 106px;
    font-size: 72px;
    color: var(--paper);
  }
  .card--back .wordmark {
    left: 0; right: 0; top: 92px;
    text-align: center;
    font-size: 98px;
    color: var(--paper);
  }

  .identity {
    position: absolute;
    left: 246px; top: 41px;
    color: var(--orange);
  }
  .identity__name {
    font-size: 27px; font-weight: 700;
    letter-spacing: 1px; line-height: 1;
  }
  .identity__role {
    font-size: 21px; font-weight: 400;
    letter-spacing: 0.6px; line-height: 1; margin-top: 6px;
  }

  .contacts {
    position: absolute;
    left: 246px; top: 131px;
    list-style: none;
    color: var(--orange);
    font-size: 15.5px;
  }
  .contacts li {
    display: flex; align-items: center;
    height: 30.5px;
  }
  .contacts svg {
    width: 20px; height: 20px;
    margin-right: 10px;
    fill: none; stroke: var(--orange); stroke-width: 1.6;
    stroke-linecap: round; stroke-linejoin: round;
  }
  .contacts svg.solid { fill: var(--orange); stroke: none; }
</style>
</head>
<body>
  <section class="card card--front">
    <div class="wordmark">KVRo</div>
    <div class="identity">
      <div class="identity__name">ALEX MORENO</div>
      <div class="identity__role">Director</div>
    </div>
    <ul class="contacts">
      <li>
        <svg viewBox="0 0 20 20"><path d="M10 18s-6-6.2-6-10a6 6 0 0 1 12 0c0 3.8-6 10-6 10z"/><circle cx="10" cy="8" r="2.2"/></svg>
        123 Street name, Your City
      </li>
      <li>
        <svg viewBox="0 0 20 20"><path d="M4 2.5l3 .2 1.5 3.8-2 1.5a10 10 0 0 0 5.5 5.5l1.5-2 3.8 1.5.2 3c-.2 1-1 1.5-2 1.5C9 17.5 2.5 11 2.5 4.5c0-1 .5-1.8 1.5-2z"/></svg>
        612 - 408 - 395- 27
      </li>
      <li>
        <svg class="solid" viewBox="0 0 20 20"><path d="M6 2l9 9.5h-4.3l2.4 5.2-2 .9-2.4-5.3L6 15.5z"/></svg>
        hello@kvro.com
      </li>
      <li>
        <svg viewBox="0 0 20 20"><rect x="1.5" y="4.5" width="17" height="11"/><path d="M1.5 4.5l8.5 7 8.5-7M1.5 15.5l6-5.5M18.5 15.5l-6-5.5"/></svg>
        www.kvro.com
      </li>
    </ul>
  </section>

  <section class="card card--back">
    <div class="wordmark">KVRo</div>
  </section>
</body>
</html>
```